Modern Spot UV Business Card design

We are a relatively new real estate agency. We need a business card that reflects the professionalism and prestige of our company but is also modern and fresh, based around our logo.
We would love to utilise spot UV.
Happy to let the designers use their imagination and see what they come up with (we're not very creative, so have no ideas for you, sorry) :-)
We'd like one for each staff member, but I've just provided one staff members photo here to avoid confusion.

Target Market(s)

Families

Industry/Entity Type

Real Estate Agent

Contact Information for Business Card

Colin Varga - Director & Principal
Mobile: 0491 527 806
Email: colin.varga@vbrokers.example.com.au
Phone: (08) 7364 9150
Fax: (08) 7364 9182
www.vargabrokersrealestate.example.com.au

Font styles to use
Other font styles liked:
• Kabel Dm BT

Requirements
Must have
• Contact details, logo, photo, spot UV
Nice to have
• Modern interesting features that will make people comment. Nothing too feminine nor too masculine.
Should not have
• No houses! Nothing typical of a real estate agent.

```html
<!DOCTYPE html>
<html lang="en">
<head>
<meta charset="utf-8">
<title>VargaBrokers Real Estate – Business Card</title>
<link href="https://fonts.googleapis.com/css2?family=Nunito:wght@400;600;800&display=swap" rel="stylesheet">
<style>
  :root {
    --card-grey: #414346;
    --page-bg: #e9e7e3;
    --white: #ffffff;
    --muted: #c9cacc;
    --orange: #f7931e;
    --photo-top: #d9dadc;
    --photo-bottom: #6b6f74;
  }
  * { box-sizing: border-box; margin: 0; padding: 0; }
  html, body { width: 1200px; height: 800px; overflow: hidden; }
  body {
    background: var(--page-bg);
    font-family: "Nunito", sans-serif;
    display: flex;
    align-items: center;
    justify-content: center;
    gap: 40px;
  }
  .card {
    position: relative;
    width: 540px;
    height: 309px;
    background: var(--card-grey);
    color: var(--white);
    overflow: hidden;
    box-shadow: 0 6px 18px rgba(0,0,0,.18);
  }

  .brand-name {
    font-weight: 800;
    color: var(--white);
    line-height: 1.05;
  }
  .brand-tagline {
    font-weight: 400;
    color: var(--muted);
    line-height: 1.15;
  }

  /* Front */
  .card-front .brand {
    position: absolute; left: 28px; top: 24px;
    width: 250px;
  }
  .card-front .brand-name { font-size: 22px; }
  .card-front .brand-tagline { font-size: 10px; margin-top: 5px; }

  .person { position: absolute; left: 28px; top: 112px; }
  .person-name { font-weight: 800; font-size: 19px; line-height: 1.2; }
  .person-title { font-weight: 600; font-size: 14px; color: var(--orange); margin-top: 1px; }

  .contact-list { list-style: none; position: absolute; left: 28px; top: 166px; }
  .contact-list li {
    display: flex; align-items: center; gap: 8px;
    font-size: 12.5px; line-height: 18px; color: var(--white);
    white-space: nowrap;
  }
  .contact-list svg { width: 12px; height: 12px; flex: none; }

  .photo {
    position: absolute; right: 0; top: 28px;
    width: 220px; height: 240px;
    background: linear-gradient(160deg, var(--photo-top), var(--photo-bottom));
  }
  .stripe-white {
    position: absolute; left: 0; bottom: 0;
    width: 300px; height: 12px; background: var(--white);
  }
  .stripe-orange {
    position: absolute; right: 0; bottom: 0;
    width: 240px; height: 12px; background: var(--orange);
  }

  /* Back */
  .card-back .brand {
    position: absolute; left: 0; right: 0; top: 96px;
    text-align: center;
  }
  .card-back .brand-name { font-size: 38px; }
  .card-back .brand-tagline { font-size: 14px; margin-top: 8px; }
  .back-web {
    position: absolute; left: 0; right: 0; bottom: 42px;
    text-align: center; font-size: 12px; color: var(--white);
  }
</style>
</head>
<body>

  <section class="card card-front" aria-label="Business card front">
    <div class="brand">
      <div class="brand-name">VargaBrokers<br>Real Estate</div>
      <div class="brand-tagline">Helping you make<br>your next move</div>
    </div>

    <div class="person">
      <div class="person-name">Colin Varga</div>
      <div class="person-title">Director &amp; Principal</div>
    </div>

    <ul class="contact-list">
      <li>
        <svg viewBox="0 0 12 12" aria-hidden="true"><rect x="3" y="0.8" width="6" height="10.4" rx="1" fill="none" stroke="var(--orange)" stroke-width="1.4"/></svg>
        0491 527 806
      </li>
      <li>
        <svg viewBox="0 0 12 12" aria-hidden="true"><path d="M1 4.5 Q6 1 11 4.5 L9.5 6 L8 5 L8 4 Q6 3.2 4 4 L4 5 L2.5 6 Z M3 7 H9 L10 11 H2 Z" fill="var(--orange)"/></svg>
        (08) 7364 9150
      </li>
      <li>
        <svg viewBox="0 0 12 12" aria-hidden="true"><rect x="3" y="1" width="6" height="4" fill="var(--orange)"/><rect x="1" y="5" width="10" height="6" rx="1" fill="var(--orange)"/></svg>
        (08) 7364 9182
      </li>
      <li>
        <svg viewBox="0 0 12 12" aria-hidden="true"><rect x="0.5" y="2" width="11" height="8" fill="var(--orange)"/><path d="M0.5 2 L6 6.5 L11.5 2" fill="none" stroke="var(--card-grey)" stroke-width="1"/></svg>
        colin.varga@vbrokers.example.com.au
      </li>
      <li>
        <svg viewBox="0 0 12 12" aria-hidden="true"><circle cx="6" cy="6" r="5.3" fill="var(--orange)"/><path d="M0.7 6 H11.3 M6 0.7 V11.3 M6 0.7 Q2.5 6 6 11.3 M6 0.7 Q9.5 6 6 11.3" fill="none" stroke="var(--card-grey)" stroke-width="0.8"/></svg>
        www.vargabrokersrealestate.example.com.au
      </li>
    </ul>

    <div class="photo" role="img" aria-label="Portrait photo of Colin Varga in a grey suit"></div>
    <div class="stripe-white"></div>
    <div class="stripe-orange"></div>
  </section>

  <section class="card card-back" aria-label="Business card back">
    <div class="brand">
      <div class="brand-name">VargaBrokers Real Estate</div>
      <div class="brand-tagline">Helping you make your next move</div>
    </div>
    <div class="back-web">www.vargabrokersrealestate.example.com.au</div>
  </section>

</body>
</html>
```